HVAC Design Services

I want a brochure to market my services. I own TOVEN Design Services LLC. I specialize in Mechanical Design with HVAC Design being my
specialty. I also do Plumbing and Civil Design. I have a strong resume with over 30 years experience. I was the Lead Mechanical Designer and Cad Manager for the mechanical group at an Architectural Engineering company for over 10 years.

I would like a professional looking brochure to pass out to engineering offices. I am targeting over-load work, when an office is so busy they need temporary help. Special project. Freeing up the engineer with my experience and capability to work with little to no direction .

1. HVAC Design
a) Calculate cfm
b) Layout and route ductwork
c) Size Ductwork
d) Choose and Layout grilles, registers and diffusers
e) Choose equipment and locate on plans
f) Create HVAC Floor Plans, Sections, Details and Schedules

2. Plumbing Design
a) Layout and route plumbing
b) Size piping
c) Create Plumbing Floor Plans, Sections, Details and Schedules.

3. CadForm 3D Modeling

4. Civil and GIS experience

5. CadForm 3D Modeling

6. Some Electrical and Structural Design experience

```html
<!DOCTYPE html>
<html lang="en">
<head>
<meta charset="utf-8">
<title>TOVEN Design Services LLC – Mechanical Design Flyer</title>
<link href="https://fonts.googleapis.com/css2?family=Roboto:wght@400;500;700&family=Lato:wght@400;700&display=swap" rel="stylesheet">
<style>
  :root{
    --green:#6cb33f;
    --green-bright:#7dc142;
    --charcoal:#333333;
    --charcoal-deep:#2b2b2b;
    --ink:#1f1f1f;
    --white:#ffffff;
    --paper:#e9e9e6;
    --photo-top:#9fb3c2;
    --photo-bottom:#c9d2d8;
  }
  *{margin:0;padding:0;box-sizing:border-box}
  html,body{width:1200px;height:800px;overflow:hidden;background:var(--paper)}
  .canvas{position:relative;width:1200px;height:800px}
  .flyer{
    position:absolute;left:307px;top:20px;width:611px;height:792px;
    transform:scale(0.96);transform-origin:top left;
    background:var(--white);overflow:hidden;
    font-family:"Lato",sans-serif;color:var(--white);
    box-shadow:0 2px 10px rgba(0,0,0,.15);
  }
  .flyer-shapes{position:absolute;left:0;top:0;width:611px;height:792px}
  .abs{position:absolute}
  .brand{left:20px;top:78px;width:210px;text-align:center;font-family:"Roboto",sans-serif;font-weight:500;color:var(--white);white-space:nowrap}
  .brand-name{font-size:26px;letter-spacing:.5px;line-height:30px}
  .brand-sub{display:flex;align-items:center;justify-content:center;gap:6px;font-size:11px;letter-spacing:3px;line-height:14px;margin-top:2px}
  .brand-sub::before,.brand-sub::after{content:"";display:block;width:26px;height:1px;background:var(--white)}
  .headline{left:30px;top:168px;font-family:"Roboto",sans-serif;font-weight:400;font-size:23.5px;line-height:29px;text-transform:uppercase;letter-spacing:.3px}
  .headline-rule{left:30px;top:266px;width:114px;height:1px;background:var(--charcoal)}
  .intro{left:27px;top:276px;width:334px;font-size:12px;line-height:17px;text-align:justify;letter-spacing:-.3px}
  .phone-main{left:388px;top:294px;display:flex;align-items:center;gap:8px;font-family:"Roboto",sans-serif;font-weight:500;font-size:23px}
  .service-col{top:362px}
  .service-col.hvac{left:26px}
  .service-col.plumbing{left:326px}
  .service-title{display:flex;align-items:flex-end;gap:10px;font-family:"Roboto",sans-serif;font-weight:400;font-size:16px;letter-spacing:.2px;height:44px;margin-bottom:12px}
  .service-list{list-style:none;font-size:11.5px;line-height:19px}
  .service-list li{display:flex;align-items:center;gap:9px;margin-left:1px}
  .tick{width:10px;height:10px;flex:none}
  .divider{left:305px;top:372px;width:1px;height:160px;background:#5a5a5a}
  .experience{left:328px;top:510px;font-family:"Roboto",sans-serif;font-size:17px;color:var(--green-bright);letter-spacing:-.2px}
  .schedule{left:28px;top:588px;font-family:"Roboto",sans-serif;font-weight:500;font-size:14px;color:var(--ink);letter-spacing:-.3px}
  .extra-list{left:322px;top:576px;list-style:none}
  .extra-list li{display:flex;align-items:center;gap:8px;height:40px;font-family:"Roboto",sans-serif;font-weight:500;font-size:13px;color:var(--charcoal);text-transform:uppercase}
  .extra-icon{width:34px;height:34px;flex:none}
  .contact{left:367px;top:715px}
  .contact-name{font-family:"Roboto",sans-serif;font-weight:700;font-size:15px;color:var(--white)}
  .contact-role{font-size:11px;color:var(--charcoal-deep);font-weight:700;margin-top:2px}
  .contact-phone{font-size:12px;color:var(--charcoal-deep);font-weight:700;display:flex;align-items:center;gap:4px;margin-top:2px}
</style>
</head>
<body>
<div class="canvas">
  <div class="flyer">
    <svg class="flyer-shapes" viewBox="0 0 611 792">
      <defs>
        <linearGradient id="gradDesigner" x1="0" y1="0" x2="0" y2="1">
          <stop offset="0" stop-color="#9fb3c2"/>
          <stop offset="1" stop-color="#d7dde0"/>
        </linearGradient>
        <linearGradient id="gradDesk" x1="0" y1="0" x2="1" y2="1">
          <stop offset="0" stop-color="#8a9099"/>
          <stop offset="1" stop-color="#c9d2d8"/>
        </linearGradient>
      </defs>
      <rect x="0" y="0" width="611" height="348" fill="#333333"/>
      <polygon points="430,0 611,0 611,280 370,280 250,138 300,95" fill="url(#gradDesigner)" role="img" aria-label="Photo of a designer drafting plans with a hard hat on the desk"/>
      <polygon points="360,0 430,0 330,83 290,83" fill="#6cb33f"/>
      <polygon points="0,138 250,138 392,280 350,348 0,348" fill="#6cb33f"/>
      <polygon points="392,280 611,280 611,348 350,348" fill="#333333"/>
      <rect x="0" y="348" width="611" height="217" fill="#2b2b2b"/>
      <polygon points="0,628 285,628 358,792 0,792" fill="url(#gradDesk)" role="img" aria-label="Photo of hands working on technical drawings beside a laptop"/>
      <polygon points="285,660 300,660 365,792 350,792" fill="#333333"/>
      <polygon points="335,707 611,707 611,775 365,775" fill="#6cb33f"/>
    </svg>

    <div class="abs brand">
      <div class="brand-name">TOVEN DESIGN</div>
      <div class="brand-sub">SERVICES LLC</div>
    </div>

    <h1 class="abs headline">Mechanical design<br>with HVAC, plumbing<br>and civil design</h1>
    <div class="abs headline-rule"></div>
    <p class="abs intro">Experienced in design layout of mechanical (HVAC/Piping) official drawings, revision drawings, shop drawings from engineer sketches and verbal information.</p>

    <div class="abs phone-main">
      <svg width="30" height="30" viewBox="0 0 30 30"><circle cx="15" cy="15" r="14" fill="#6cb33f"/><circle cx="15" cy="15" r="10" fill="none" stroke="#ffffff" stroke-width="1.6"/><path d="M11.5 10.5c.6-.6 1.3-.5 1.7.1l1 1.6c.3.5.2 1-.2 1.4l-.6.5c.5 1.1 1.4 2 2.5 2.5l.5-.6c.4-.4.9-.5 1.4-.2l1.6 1c.6.4.7 1.1.1 1.7-1 1-2.4 1.1-3.7.4-2.2-1.2-3.6-2.6-4.7-4.7-.7-1.3-.6-2.7.4-3.7z" fill="#ffffff"/></svg>
      <span>(555)-014-2780</span>
    </div>

    <section class="abs service-col hvac">
      <h2 class="service-title">
        <svg width="44" height="44" viewBox="0 0 44 44" fill="none" stroke="#6cb33f" stroke-width="1.6"><circle cx="22" cy="6" r="3"/><path d="M22 9 L10 40 M22 9 L34 40 M13 30 Q22 36 31 30 M4 42 H40"/></svg>
        HVAC DESIGN
      </h2>
      <ul class="service-list">
        <li><svg class="tick" viewBox="0 0 10 10"><circle cx="5" cy="5" r="5" fill="#6cb33f"/><path d="M2.6 5.1 4.3 6.7 7.4 3.4" stroke="#ffffff" stroke-width="1.3" fill="none"/></svg>Calculate cfm</li>
        <li><svg class="tick" viewBox="0 0 10 10"><circle cx="5" cy="5" r="5" fill="#6cb33f"/><path d="M2.6 5.1 4.3 6.7 7.4 3.4" stroke="#ffffff" stroke-width="1.3" fill="none"/></svg>Layout and route ductwork</li>
        <li><svg class="tick" viewBox="0 0 10 10"><circle cx="5" cy="5" r="5" fill="#6cb33f"/><path d="M2.6 5.1 4.3 6.7 7.4 3.4" stroke="#ffffff" stroke-width="1.3" fill="none"/></svg>Size Ductwork</li>
        <li><svg class="tick" viewBox="0 0 10 10"><circle cx="5" cy="5" r="5" fill="#6cb33f"/><path d="M2.6 5.1 4.3 6.7 7.4 3.4" stroke="#ffffff" stroke-width="1.3" fill="none"/></svg>Choose and Layout grilles, registers and diffusers</li>
        <li><svg class="tick" viewBox="0 0 10 10"><circle cx="5" cy="5" r="5" fill="#6cb33f"/><path d="M2.6 5.1 4.3 6.7 7.4 3.4" stroke="#ffffff" stroke-width="1.3" fill="none"/></svg>Choose equipment and locate on plans</li>
        <li><svg class="tick" viewBox="0 0 10 10"><circle cx="5" cy="5" r="5" fill="#6cb33f"/><path d="M2.6 5.1 4.3 6.7 7.4 3.4" stroke="#ffffff" stroke-width="1.3" fill="none"/></svg>Create HVAC Floor Plans, Sections,</li>
        <li><svg class="tick" viewBox="0 0 10 10"><circle cx="5" cy="5" r="5" fill="#6cb33f"/><path d="M2.6 5.1 4.3 6.7 7.4 3.4" stroke="#ffffff" stroke-width="1.3" fill="none"/></svg>Details and Schedules</li>
      </ul>
    </section>

    <div class="abs divider"></div>

    <section class="abs service-col plumbing">
      <h2 class="service-title">
        <svg width="28" height="44" viewBox="0 0 28 44" fill="none" stroke="#6cb33f" stroke-width="1.6"><path d="M6 42 V16 Q6 4 16 4 Q24 4 24 12 V16 M20 16 H28 M3 42 H13 M6 26 H12 V34 H6"/><path d="M24 22 v3 M24 29 v3" stroke-dasharray="2 2"/></svg>
        PLUMBING DESIGN
      </h2>
      <ul class="service-list">
        <li><svg class="tick" viewBox="0 0 10 10"><circle cx="5" cy="5" r="5" fill="#6cb33f"/><path d="M2.6 5.1 4.3 6.7 7.4 3.4" stroke="#ffffff" stroke-width="1.3" fill="none"/></svg>Layout and route plumbing</li>
        <li><svg class="tick" viewBox="0 0 10 10"><circle cx="5" cy="5" r="5" fill="#6cb33f"/><path d="M2.6 5.1 4.3 6.7 7.4 3.4" stroke="#ffffff" stroke-width="1.3" fill="none"/></svg>Size piping</li>
        <li><svg class="tick" viewBox="0 0 10 10"><circle cx="5" cy="5" r="5" fill="#6cb33f"/><path d="M2.6 5.1 4.3 6.7 7.4 3.4" stroke="#ffffff" stroke-width="1.3" fill="none"/></svg>Create Plumbing Floor Plans,</li>
        <li><svg class="tick" viewBox="0 0 10 10"><circle cx="5" cy="5" r="5" fill="#6cb33f"/><path d="M2.6 5.1 4.3 6.7 7.4 3.4" stroke="#ffffff" stroke-width="1.3" fill="none"/></svg>Sections, Details and Schedules</li>
      </ul>
    </section>

    <p class="abs experience">OVER 30 YEARS EXPERIENCE</p>

    <p class="abs schedule">SCHEDULE YOUR APPOINTMENT TODAY</p>

    <ul class="abs extra-list">
      <li><svg class="extra-icon" viewBox="0 0 34 34"><circle cx="17" cy="17" r="16" fill="#333333"/><circle cx="17" cy="17" r="12" fill="none" stroke="#6cb33f" stroke-width="1.2"/><path d="M11 12 h8 l4 4 v7 h-12 z M19 12 v4 h4" fill="none" stroke="#6cb33f" stroke-width="1.2"/></svg>CadForm 3D Modeling</li>
      <li><svg class="extra-icon" viewBox="0 0 34 34"><circle cx="17" cy="17" r="16" fill="#333333"/><circle cx="17" cy="17" r="12" fill="none" stroke="#6cb33f" stroke-width="1.2"/><circle cx="17" cy="17" r="4" fill="none" stroke="#6cb33f" stroke-width="1.2"/><path d="M17 9 v3 M17 22 v3 M9 17 h3 M22 17 h3" stroke="#6cb33f" stroke-width="1.2"/></svg>Civil and GIS</li>
      <li><svg class="extra-icon" viewBox="0 0 34 34"><circle cx="17" cy="17" r="16" fill="#333333"/><circle cx="17" cy="17" r="12" fill="none" stroke="#6cb33f" stroke-width="1.2"/><path d="M17 10 a5 5 0 0 1 3 9 v3 h-6 v-3 a5 5 0 0 1 3 -9 z M15 24 h4" fill="none" stroke="#6cb33f" stroke-width="1.2"/></svg>Electrical &amp; Structural Design</li>
    </ul>

    <div class="abs contact">
      <div class="contact-name">MARCO DELGADO</div>
      <div class="contact-role">Sr. MECHANICAL/CIVIL PROJECT DESIGNER</div>
      <div class="contact-phone">
        <svg width="11" height="11" viewBox="0 0 30 30"><circle cx="15" cy="15" r="13" fill="none" stroke="#2b2b2b" stroke-width="2.5"/><path d="M11.5 10.5c.6-.6 1.3-.5 1.7.1l1 1.6c.3.5.2 1-.2 1.4l-.6.5c.5 1.1 1.4 2 2.5 2.5l.5-.6c.4-.4.9-.5 1.4-.2l1.6 1c.6.4.7 1.1.1 1.7-1 1-2.4 1.1-3.7.4-2.2-1.2-3.6-2.6-4.7-4.7-.7-1.3-.6-2.7.4-3.7z" fill="#2b2b2b"/></svg>
        (555)-014-2780
      </div>
    </div>
  </div>
</div>
</body>
</html>
```